Community Youth Organisation needs a flyer template design for youth workshop

We require a flyer design that can be used for ongoing youth workshops targetted at young people 11-19 with intellectual disabilities (including Autism and Aspergers). We are hoping the flyer can be used over and over again when advertising our upcoming youth workshop series. Each workshop series will be approx 5 weeks and will be based on a particular topic. For example, our first workshop series will be run every Monday afternoon for 5 weeks on the topic "Conflict and Anger Management" (see attached info). We will then run a different workshop series on a different topic so we would like the same design to be used however with the possibility of editing the specific workshop info on it (e.g. dates, topic). We would require our BRTW logo on the flyer and graphics that would grab the attention of young people aged 11-19 with intellectual disabilities.

Target Market(s)

young people aged 11-19 with intellectual disabilities and their parents/carers

Industry/Entity Type

Advertising

Requirements
Must have
• BRTW Logo as prominent
Information as provided in attachment however in any "look" you feel would be appealing to the target group

```html
<!DOCTYPE html>
<html lang="en">
<head>
<meta charset="utf-8">
<title>BRTW Youth Workshop – Conflict and Anger Management</title>
<link rel="stylesheet" href="https://fonts.googleapis.com/css2?family=Bree+Serif&family=Open+Sans:ital,wght@0,400;0,600;0,700;0,800;1,400&display=swap">
<style>
  :root {
    --navy: #1f3a6e;
    --blue: #2b5aa0;
    --orange: #ee7d24;
    --magenta: #d4246f;
    --ink: #26324a;
    --paper-top: #ffffff;
    --paper-bottom: #dcebf6;
    --tree-warm: #f3b35a;
    --tree-cool: #7fb8d9;
    --white: #ffffff;
  }
  html, body {
    margin: 0;
    padding: 0;
    overflow: hidden;
  }
  .flyer {
    position: relative;
    width: 857px;
    height: 1200px;
    overflow: hidden;
    background: linear-gradient(180deg, var(--paper-top) 0%, var(--paper-top) 25%, var(--paper-bottom) 100%);
    font-family: "Open Sans", Arial, sans-serif;
    color: var(--ink);
  }
  .kicker {
    position: absolute;
    top: 12px;
    left: 0;
    width: 857px;
    margin: 0;
    text-align: center;
    font-weight: 700;
    font-size: 31px;
    line-height: 40px;
    color: var(--navy);
  }
  .title {
    position: absolute;
    top: 58px;
    left: 0;
    width: 857px;
    margin: 0;
    text-align: center;
    font-family: "Bree Serif", Georgia, serif;
    font-weight: 400;
    font-size: 54px;
    line-height: 56px;
    color: var(--orange);
  }
  .intro {
    position: absolute;
    top: 180px;
    left: 30px;
    width: 797px;
    margin: 0;
    text-align: center;
    font-size: 16.5px;
    line-height: 22px;
    color: var(--ink);
  }
  .tree-art {
    position: absolute;
    top: 300px;
    left: 0;
    width: 545px;
    height: 625px;
    background:
      radial-gradient(ellipse 55% 42% at 45% 40%, var(--tree-warm) 0%, rgba(243,179,90,0.55) 45%, rgba(127,184,217,0.25) 75%, rgba(220,235,246,0) 100%),
      linear-gradient(180deg, rgba(255,255,255,0) 60%, rgba(150,110,70,0.35) 100%);
  }
  .tea-badge {
    position: absolute;
    top: 302px;
    left: 95px;
    width: 165px;
    height: 118px;
    border-radius: 50%;
    background: var(--orange);
    color: var(--white);
    display: flex;
    align-items: center;
    justify-content: center;
    text-align: center;
    font-weight: 700;
    font-size: 20px;
    line-height: 24px;
    transform: rotate(-12deg);
  }
  .schedule {
    position: absolute;
    top: 328px;
    left: 360px;
    width: 480px;
    margin: 0;
    text-align: center;
    font-weight: 800;
    font-size: 27px;
    line-height: 31px;
    color: var(--magenta);
  }
  .venue {
    position: absolute;
    top: 456px;
    left: 540px;
    width: 300px;
    margin: 0;
    text-align: center;
    font-weight: 700;
    font-size: 24px;
    line-height: 30px;
    color: var(--blue);
    font-style: normal;
  }
  .outcomes {
    position: absolute;
    top: 566px;
    left: 560px;
    width: 280px;
    margin: 0;
    text-align: center;
    font-size: 17px;
    line-height: 24px;
    color: var(--ink);
  }
  .register-band {
    position: absolute;
    left: 0;
    top: 925px;
    width: 857px;
    height: 275px;
    background: var(--navy);
  }
  .register-text {
    position: absolute;
    left: 28px;
    top: 24px;
    width: 560px;
    margin: 0;
    color: var(--white);
    font-weight: 700;
    font-size: 23px;
    line-height: 31px;
  }
  .fine-print {
    position: absolute;
    left: 28px;
    top: 238px;
    width: 560px;
    margin: 0;
    color: var(--white);
    font-size: 9.5px;
    line-height: 11px;
  }
  .brand-tile {
    position: absolute;
    right: 0;
    top: 40px;
    width: 245px;
    height: 130px;
    background: var(--white);
    border-radius: 14px 0 0 14px;
    display: flex;
    align-items: center;
    justify-content: center;
    gap: 12px;
  }
  .brand-dot {
    width: 34px;
    height: 34px;
    border-radius: 50%;
    background: var(--orange);
  }
  .brand-name {
    font-weight: 800;
    font-size: 46px;
    color: var(--navy);
  }
</style>
</head>
<body>
<main class="flyer">
  <p class="kicker">BRTW presents a youth workshop in</p>
  <h1 class="title">Conflict and Anger<br>management</h1>
  <p class="intro">Workshops provide young people between the ages of 11 -19 years with intellectual disabilities as well as those with Autism Spectrum Disorder, Asperger's, and ADHD,with an opportunity to socialise with their peers while learning essential life skills. They include a combination of hands on activities, group work and discussion.</p>

  <div class="tree-art" role="img" aria-label="Illustration of a tree whose trunk is a raised arm and whose leaves are colourful handprints"></div>
  <div class="tea-badge">Afternoon<br>Tea Free<br>of Charge</div>

  <p class="schedule">Mon 15th, 22nd, 29th April<br>Mon 6th, 13th May<br>2013<br>3.15pm - 5pm</p>

  <address class="venue">BRTW<br>42 Wattle Lane,<br>Riverton 4310</address>

  <p class="outcomes">During the workshops participants will learn to identify the physical and emotional symptoms of anger, understand what their personal triggers are, learn techniques to express their emotions in a positive manner and discover appropriate ways to respond to bullying behaviours.</p>

  <footer class="register-band">
    <p class="register-text">To register simply contact Dana Morrow, Youth and Family Worker via phone 3900 4411 or email hello@brtw.org.au</p>
    <p class="fine-print">Places are limited and offered in order of registration. By registering, participants agree to attend every session in the series where possible.</p>
    <div class="brand-tile">
      <span class="brand-dot"></span>
      <span class="brand-name">BRTW</span>
    </div>
  </footer>
</main>
</body>
</html>
```